Norvexa Site

We are looking for someone to help build a information site of our product Norvexa for Sickle Cell Disease

Industry/Entity Type

Patent Educational Site

Coding

Coded - Design and coding required

Number of Pages Required

5+ page

Font styles to use
Sans Serif

Colors
EB3D1F
EC4F4E
F09395
F8D3D4
FCEDEE

```html
<!DOCTYPE html>
<html lang="en">
<head>
<meta charset="utf-8">
<title>Norvexa – Sickle Cell Disease</title>
<link href="https://fonts.googleapis.com/css2?family=Roboto:ital,wght@0,300;0,400;0,500;0,700;0,900;1,400&family=Oswald:wght@600&display=swap" rel="stylesheet">
<style>
:root{
  --brand-deep:#b62a2e;
  --brand:#ec4f4e;
  --brand-soft:#f09395;
  --brand-pale:#f8d3d4;
  --brand-mist:#fcedee;
  --ink:#333333;
  --text:#444444;
  --muted:#777777;
  --white:#ffffff;
}
*{margin:0;padding:0;box-sizing:border-box}
html,body{width:1200px;height:3124px;overflow:hidden}
body{font-family:"Roboto",sans-serif;color:var(--text);background:var(--white)}
.page{position:relative;width:1200px;height:3124px}
.abs{position:absolute}

.topbar{left:0;top:0;width:1200px;height:25px;background:var(--brand-deep);color:var(--white);font-size:11px}
.topbar .contact{left:160px;top:6px;display:flex;gap:22px}
.topbar .follow{right:161px;top:6px;display:flex;align-items:center;gap:6px}
.topbar .sq{width:10px;height:10px;background:var(--white);border-radius:2px}

.header{left:0;top:25px;width:1200px;height:78px;background:var(--white)}
.logo{left:160px;top:10px;width:170px}
.logo .name{font-size:44px;font-weight:400;color:var(--brand-deep);letter-spacing:2px;line-height:44px}
.logo .by{font-size:14px;color:var(--ink);margin-left:84px;margin-top:-4px}
.nav{right:162px;top:32px;display:flex;gap:17px;font-size:13px;color:var(--ink)}

.hero{left:0;top:103px;width:1200px;height:516px;background:linear-gradient(100deg,#cfd9de 0%,#9fb7c4 30%,#e8d6c6 55%,#c9b7a5 80%,#8f9aa0 100%)}
.hero h1{left:0;width:1200px;top:340px;text-align:center;font-family:"Oswald",sans-serif;font-size:60px;color:var(--white);letter-spacing:0;text-shadow:0 2px 6px rgba(0,0,0,.35)}
.hero .pill{left:456px;top:404px;width:286px;height:40px;border-radius:20px;background:var(--brand);color:var(--white);font-size:15px;display:flex;align-items:center;justify-content:center}

.welcome-photo{left:160px;top:669px;width:394px;height:434px;background:linear-gradient(160deg,#dfe6ea,#aeb9c6 50%,#5f7ea8)}
.badge{left:373px;top:1063px;width:191px;height:74px;background:var(--white);box-shadow:0 4px 14px rgba(0,0,0,.12);display:flex;align-items:center;gap:10px;padding:0 14px}
.badge .ic{width:46px;height:46px;background:var(--brand-soft);border-radius:3px;display:flex;align-items:center;justify-content:center}
.badge b{display:block;font-weight:400;font-size:14px;color:var(--ink)}
.badge small{font-size:10px;color:var(--muted)}
.welcome-text{left:606px;top:667px;width:432px}
.welcome-text .kicker{font-size:23px;font-weight:500;color:var(--ink);line-height:24px;margin-left:2px}
.welcome-text h2{font-size:54px;font-weight:700;color:var(--brand-deep);line-height:52px;margin-bottom:8px}
.welcome-text p{font-size:12.6px;line-height:19.5px;margin-bottom:8px}
.mission{display:flex;gap:15px;margin:24px 0 10px}
.mission .ic{flex:none;width:50px;height:50px;background:var(--brand-soft);display:flex;align-items:center;justify-content:center}
.mission h3{font-size:14.5px;font-weight:500;color:var(--ink)}

.features{left:0;top:1191px;width:1200px;height:165px;background:var(--brand-soft);display:flex;padding:0 160px;justify-content:space-between}
.feature{width:170px;text-align:center;color:var(--white);padding-top:26px}
.feature svg{display:block;margin:0 auto 6px}
.feature h4{font-size:17px;font-weight:700;margin-bottom:4px}
.feature p{font-size:12px;line-height:17px;color:#fff4f4}

.cards{left:160px;top:1405px;width:880px;display:flex;gap:19px}
.card{width:280px;height:312px;border-radius:10px;overflow:hidden;background:var(--brand-deep)}
.card .img{height:252px}
.card span{display:block;text-align:center;color:var(--white);font-size:16.5px;font-weight:500;line-height:60px}

.split{left:0;top:1774px;width:1200px;height:289px;display:flex}
.split .pane{position:relative;height:289px}
.pane.dark{width:606px;background:var(--ink)}
.pane.red{width:594px;background:var(--brand)}
.pane .circle{position:absolute;top:49px;width:74px;height:74px;border-radius:50%;background:var(--white);display:flex;align-items:center;justify-content:center}
.pane h3{position:absolute;top:54px;font-size:23px;font-weight:500;color:var(--white)}
.pane p{position:absolute;top:88px;width:310px;font-size:12.5px;line-height:19px;color:var(--white)}
.pane .btn{position:absolute;top:186px;width:114px;height:38px;border:1px solid var(--white);border-radius:19px;color:var(--white);font-size:11.5px;display:flex;align-items:center;justify-content:center}

.testi-title{left:0;width:1200px;top:2106px;text-align:center;font-size:43px;font-weight:700;color:var(--ink)}
.tcard{top:2194px;width:426px;height:220px;background:var(--white);box-shadow:0 2px 10px rgba(0,0,0,.08);border-bottom:9px solid var(--brand-soft);text-align:center}
.tcard .q{position:absolute;font-size:150px;font-weight:900;color:#f0f0f0;line-height:1;font-family:Georgia,serif}
.tcard .avatar{position:relative;width:72px;height:72px;border-radius:50%;margin:14px auto 8px;border:2px solid #ddd}
.tcard p{position:relative;font-size:12px;font-style:italic;line-height:18px;padding:0 30px;color:#555;height:73px;overflow:hidden}
.tcard h5{position:relative;font-size:12px;font-weight:500;color:var(--ink);margin-top:14px}
.dots{left:560px;top:2460px;display:flex;gap:7px}
.dots i{width:13px;height:13px;border-radius:50%;border:1px solid #999}
.dots i:first-child{background:var(--ink);border-color:var(--ink)}

.contact{left:0;top:2531px;width:1200px;height:532px;background:linear-gradient(90deg,#f1f4f6 0%,#e6ecf0 60%,#dfe7ec 100%)}
.contact .doctor{right:0;top:0;width:380px;height:532px;background:linear-gradient(180deg,#e9eef1,#d4e3ea 40%,#c5d5df);}
.contact h2{left:160px;top:56px;font-size:52px;font-weight:700;color:var(--ink)}
.contact .sub{left:161px;top:118px;font-size:14px;color:var(--text)}
.field{position:absolute;border:1px solid #aaa;background:rgba(255,255,255,.35);font-size:11px;color:#666;padding:0 15px;display:flex;align-items:center}
.send{left:161px;top:2942px;width:186px;height:56px;border-radius:28px;background:var(--brand);color:var(--white);font-size:17px;font-weight:500;display:flex;align-items:center;justify-content:center}

.footer{left:0;top:3063px;width:1200px;height:61px;background:var(--brand-deep);color:var(--white)}
.footer .copy{left:160px;top:24px;font-size:11px}
.footer .social{right:161px;top:15px;display:flex;gap:6px}
.footer .social i{width:30px;height:30px;border-radius:50%;border:1px solid var(--white)}
</style>
</head>
<body>
<div class="page">

  <div class="abs topbar">
    <div class="abs contact"><span>✉ info@norvexabyvelmora.com</span><span>✆ (555) 014-2290</span></div>
    <div class="abs follow"><span>FOLLOW US</span><i class="sq"></i><i class="sq"></i><i class="sq"></i></div>
  </div>

  <header class="abs header">
    <div class="abs logo"><div class="name">Norvexa</div><div class="by">By Velmora</div></div>
    <nav class="abs nav"><span>WHAT IS NORVEXA</span><span>ABOUT SCD</span><span>HOW NORVEXA WORKS</span><span>INSURANCE COVERAGE</span><span>PATIENT SUPPORT</span></nav>
  </header>

  <section class="abs hero" role="img" aria-label="Doctor with tablet smiling at a young girl held by her mother in a clinic">
    <h1 class="abs">SICKLE CELL DISEASE</h1>
    <div class="abs pill">IN PEDIATRIC AND ADULT PATIENTS</div>
  </section>

  <div class="abs welcome-photo" role="img" aria-label="Nurse assisting a smiling senior man in a wheelchair"></div>
  <div class="abs badge">
    <div class="ic"><svg width="30" height="30" viewBox="0 0 30 30" fill="none" stroke="#fff" stroke-width="1.6"><path d="M15 10c-2-4-8-3-8 1 0 4 8 9 8 9s8-5 8-9c0-4-6-5-8-1z"/><path d="M3 14v8l6 5M27 14v8l-6 5"/></svg></div>
    <div><b>More Than 24 +</b><small>Years of Experience</small></div>
  </div>
  <div class="abs welcome-text">
    <div class="kicker">WELCOME TO</div>
    <h2>NORVEXA</h2>
    <p>Lorem Ipsum is simply dummy text of the printing and typesetting industry. Lorem Ipsum has been the industry's standard dummy text ever since the make a type specimen book. It has survived not only five centuries, but also the leap into electronic typesetting, remaining essentially unchanged. It was Lorem Ipsum passages, and more recently with desktop publishing software like Quillset Layout including versions of Lorem Ipsum.</p>
    <p>Lorem Ipsum is simply dummy text of the printing and typesetting industry. Lorem Ipsum has been the industry's standard dummy text ever since the make a type specimen book. It has survived not only five centuries, but also the leap into electronic typesetting, remaining essentially unchanged. It was Lorem Ipsum passages, and more recently with desktop publishing software like Quillset Layout including versions of Lorem Ipsum.</p>
    <div class="mission">
      <div class="ic"><svg width="32" height="32" viewBox="0 0 32 32" fill="none" stroke="#fff" stroke-width="1.8"><circle cx="15" cy="17" r="12"/><circle cx="15" cy="17" r="7"/><circle cx="15" cy="17" r="2"/><path d="M15 17l12-12M23 5h4v4"/></svg></div>
      <div><h3>Our Mission</h3><p>Lorem Ipsum is simply dummy text of the printing and typesetting software like Quillset Layout including of Lorem Ipsum.</p></div>
    </div>
    <p>Lorem Ipsum is simply dummy text of the printing and typesetting industry. Lorem Ipsum passages, and more recently with desktop publishing software like Quillset Layout including versions of Lorem Ipsum.</p>
  </div>

  <section class="abs features">
    <div class="feature"><svg width="40" height="40" viewBox="0 0 40 40" fill="none" stroke="#fff" stroke-width="2.2"><circle cx="22" cy="20" r="12"/><path d="M6 10c-2 8 4 20 14 24l4-4-5-4-3 2c-3-2-5-5-6-8l2-3-4-5z" fill="#fff"/><text x="22" y="24" font-size="10" fill="#fff" stroke="none" text-anchor="middle" font-family="Roboto,sans-serif" font-weight="700">24</text></svg><h4>24/7 SERVICE</h4><p>Lorem Ipsum is simply dummy text printing industry.</p></div>
    <div class="feature"><svg width="40" height="40" viewBox="0 0 40 40" fill="#fff"><circle cx="20" cy="12" r="7"/><path d="M6 36c0-9 6-14 14-14s14 5 14 14z"/></svg><h4>PROFESSIONAL</h4><p>Lorem Ipsum is simply dummy text printing industry.</p></div>
    <div class="feature"><svg width="40" height="40" viewBox="0 0 40 40" fill="none" stroke="#fff" stroke-width="2"><circle cx="22" cy="15" r="8"/><text x="22" y="19" font-size="11" fill="#fff" stroke="none" text-anchor="middle" font-family="Roboto,sans-serif">$</text><path d="M4 30h8l8 3 14-6M22 3v-2"/></svg><h4>AFFORDABLE</h4><p>Lorem Ipsum is simply dummy text printing industry.</p></div>
    <div class="feature"><svg width="40" height="40" viewBox="0 0 40 40" fill="none" stroke="#fff" stroke-width="2.4"><circle cx="20" cy="20" r="12"/><path d="M14 20l4 4 8-8"/></svg><h4>GUARANTEED</h4><p>Lorem Ipsum is simply dummy text printing industry.</p></div>
  </section>

  <section class="abs cards">
    <div class="card"><div class="img" role="img" aria-label="Mother giving medicine to her child with a spoon" style="background:linear-gradient(135deg,#e8e4df,#b08a6e 60%,#6b4a35)"></div><span>What is Norvexa</span></div>
    <div class="card"><div class="img" role="img" aria-label="Close-up of a red blood cell on black" style="background:radial-gradient(circle at 40% 40%,#e4202a,#9a0d14 50%,#1a0000 75%,#000)"></div><span>How Norvexa Works</span></div>
    <div class="card"><div class="img" role="img" aria-label="Two women reviewing insurance documents at a desk" style="background:linear-gradient(135deg,#eceae6,#c9c2b8 50%,#8e8a86)"></div><span>Insurance Coverage</span></div>
  </section>

  <section class="abs split">
    <div class="pane dark">
      <div class="circle" style="left:160px"><svg width="44" height="44" viewBox="0 0 44 44" fill="none" stroke="#333" stroke-width="2"><path d="M22 14c-3-5-10-3-10 2 0 5 10 11 10 11s10-6 10-11c0-5-7-7-10-2z"/><path d="M22 15v8M18 19h8M4 18v12l8 8M40 18v12l-8 8"/></svg></div>
      <h3 style="left:251px">About Sickle Cell Disease</h3>
      <p style="left:251px">Lorem Ipsum is simply dummy text of the printing and typesetting industry. Lorem Ipsum has been the industry recently with desktop publishing software like Quillset Layout including versions of Lorem Ipsum.</p>
      <div class="btn" style="left:251px">READ MORE</div>
    </div>
    <div class="pane red">
      <div class="circle" style="left:40px"><svg width="44" height="44" viewBox="0 0 44 44" fill="none" stroke="#ec4f4e" stroke-width="2"><circle cx="22" cy="16" r="8"/><path d="M12 16a10 10 0 0 1 20 0M10 40c0-8 5-12 12-12s12 4 12 12zM32 18v3l-6 2"/></svg></div>
      <h3 style="left:132px">Patient Support</h3>
      <p style="left:132px">Lorem Ipsum is simply dummy text of the printing and typesetting industry. Lorem Ipsum has been the industry recently with desktop publishing software like Quillset Layout including versions of Lorem Ipsum.</p>
      <div class="btn" style="left:133px">READ MORE</div>
    </div>
  </section>

  <h2 class="abs testi-title">TESTIMONIALS</h2>
  <div class="abs tcard" style="left:160px">
    <span class="q" style="left:20px;top:0">“</span><span class="q" style="right:20px;bottom:-70px">”</span>
    <div class="avatar" role="img" aria-label="Portrait of a grey-haired man" style="background:linear-gradient(#e6e9ec,#b9c2cb)"></div>
    <p>Lorem Ipsum is simply dummy text of the printing and typesetting industry. Lorem Ipsum has been the industry's standard dummy text ever since the 1500s, when an unknown printer took a galley of type and scrambled it to make a type specimen book. It has survived not</p>
    <h5>LENA MARSH</h5>
  </div>
  <div class="abs tcard" style="left:613px">
    <span class="q" style="left:20px;top:0">“</span><span class="q" style="right:20px;bottom:-70px">”</span>
    <div class="avatar" role="img" aria-label="Portrait of a blonde woman" style="background:linear-gradient(#f2e6d4,#d9b88e)"></div>
    <p>Lorem Ipsum is simply dummy text of the printing and typesetting industry. Lorem Ipsum has been the industry's standard dummy text ever since the 1500s, when an unknown printer took a galley of type and scrambled it to make a type specimen book.</p>
    <h5>OWEN PRICE</h5>
  </div>
  <div class="abs dots"><i></i><i></i><i></i><i></i></div>

  <section class="abs contact">
    <div class="abs doctor" role="img" aria-label="Doctor in a white coat holding a stethoscope"></div>
    <h2 class="abs">GET IN TOUCH</h2>
    <div class="abs sub">Your request will be answered withing 24 hours</div>
    <div class="field" style="left:161px;top:140px;width:288px;height:50px">Enter your name</div>
    <div class="field" style="left:461px;top:140px;width:288px;height:50px">Enter your phone</div>
    <div class="field" style="left:161px;top:201px;width:288px;height:50px">Enter your email</div>
    <div class="field" style="left:461px;top:201px;width:288px;height:50px">Enter your address</div>
    <div class="field" style="left:161px;top:262px;width:588px;height:124px;align-items:flex-start;padding-top:22px">Enter your comments</div>
  </section>
  <div class="abs send">SEND MESSAGE</div>

  <footer class="abs footer">
    <div class="abs copy">COPYRIGHT © 2023 NORVEXA.COM. ALL RIGHTS RESERVED</div>
    <div class="abs social"><i></i><i></i><i></i><i></i></div>
  </footer>

</div>
</body>
</html>
```